Simple, elegant, business card design required

Hi designers,I am looking for a simple yet elegant business card design.

Please make use of my logo (attached); you are free to tweak the logo should you wish to do so.

Our business is involved in many different fields - almost all of them involved in some form of "design", so that's really one of the key things I want to portray. I do not wish to specify which field of design, exactly.

I prefer white on black (or just monochromatic), but if you have a different, creative idea, I am open to that too.

You can use artsy photographs provided that you have the license to use those. Please feel free to ask me any questions.
Updates

Project Deadline Extended Reason: Small extension for potential revisions. Did not get the time to provide as much feedback as I can. Added Wednesday, July 09, 2014

Target Market(s)

High-end customers looking for design consultancy

Industry/Entity Type

Business

Contact Information for Business Card

Name: Gareth Moonfield
Position: Creative Director
Mobile: +155603928174
Address: Barrow Lane, Ashbury Vale, Dunmorshire GL12 4RT
Website: torvakest.com (not launched yet)

Requirements
Must have
• Design layout must be clean, original, and text must be readable when printed.
Should not have
• ~ No business card templates please. Anyone using this will be reported.
• ~ Please don't spam entries.

```html
<!DOCTYPE html>
<html lang="en">
<head>
<meta charset="utf-8">
<title>Torvakest Business Card</title>
<link rel="stylesheet" href="https://fonts.googleapis.com/css2?family=Open+Sans:wght@400;700&family=Oswald:wght@400&display=swap">
<style>
  :root {
    --ink: #1c1c1c;
    --paper: #ffffff;
    --stage: #e4e2df;
    --muted: #3a3a3a;
    --shadow: rgba(0, 0, 0, 0.22);
  }
  * { margin: 0; padding: 0; box-sizing: border-box; }
  html, body {
    width: 1200px;
    height: 829px;
    overflow: hidden;
    background: var(--stage);
  }
  .canvas {
    position: relative;
    width: 1200px;
    height: 829px;
  }
  .card {
    position: absolute;
    width: 560px;
    height: 320px;
    box-shadow: 0 6px 18px var(--shadow);
    overflow: hidden;
  }

  /* Front: personal details */
  .card--front {
    left: 70px;
    top: 80px;
    background: var(--paper);
  }
  .name-band {
    position: absolute;
    left: 0;
    top: 178px;
    width: 262px;
    height: 56px;
    background: var(--ink);
    padding: 9px 0 0 34px;
    color: var(--paper);
  }
  .name-band__name {
    font-family: "Open Sans", sans-serif;
    font-weight: 700;
    font-size: 17px;
    line-height: 1.2;
  }
  .name-band__role {
    font-family: "Open Sans", sans-serif;
    font-weight: 400;
    font-size: 12px;
    line-height: 1.4;
  }
  .brand-square {
    position: absolute;
    left: 270px;
    top: 54px;
    width: 112px;
    height: 88px;
    background: var(--ink);
  }
  .brand-name {
    position: absolute;
    font-family: "Oswald", sans-serif;
    font-weight: 400;
    color: var(--ink);
    letter-spacing: 0.28em;
    white-space: nowrap;
  }
  .card--front .brand-name {
    left: 396px;
    top: 50px;
    font-size: 20px;
  }
  .contact {
    position: absolute;
    right: 30px;
    top: 160px;
    font-family: "Open Sans", sans-serif;
    font-size: 12.5px;
    color: var(--muted);
    text-align: right;
    line-height: 1.75;
    list-style: none;
  }
  .contact__item {
    display: flex;
    justify-content: flex-end;
    align-items: center;
    gap: 7px;
  }
  .contact__icon { width: 11px; height: 11px; fill: var(--muted); }
  .contact__address { margin-top: 8px; line-height: 1.55; }

  /* Back: brand */
  .card--back {
    left: 570px;
    top: 430px;
    background: var(--ink);
    color: var(--paper);
  }
  .card--back .brand-name {
    left: 250px;
    top: 108px;
    font-size: 40px;
    color: var(--paper);
  }
  .back-web {
    position: absolute;
    left: 254px;
    top: 172px;
    font-family: "Open Sans", sans-serif;
    font-size: 17px;
    letter-spacing: 0.04em;
  }
</style>
</head>
<body>
<main class="canvas">

  <section class="card card--front" aria-label="Business card front">
    <div class="brand-square"></div>
    <p class="brand-name">TORVAKEST</p>

    <div class="name-band">
      <p class="name-band__name">Gareth Moonfield</p>
      <p class="name-band__role">Creative Director</p>
    </div>

    <ul class="contact">
      <li class="contact__item">
        <svg class="contact__icon" viewBox="0 0 12 12" aria-hidden="true"><rect x="3" y="0.5" width="6" height="11" rx="1.2"/></svg>
        <span>+1556-0392-8174</span>
      </li>
      <li class="contact__item">
        <svg class="contact__icon" viewBox="0 0 12 12" aria-hidden="true"><circle cx="6" cy="6" r="5.5"/></svg>
        <span>www.torvakest.com</span>
      </li>
      <li class="contact__address">Barrow Lane, Ashbury Vale<br>Dunmorshire GL12 4RT</li>
    </ul>
  </section>

  <section class="card card--back" aria-label="Business card back">
    <p class="brand-name">TORVAKEST</p>
    <p class="back-web">www.torvakest.com</p>
  </section>

</main>
</body>
</html>
```